Website on Hubspot CMS -Boutique consulting firm focused on the events and event tech industries

Design website for our business using Hubspot CMS. Some pages already done. We would like those tweaked to match your recommended design. We also would like landing pages created for four business services offerings. We have a color palette and logo.

Our current website can be found here: www.qlvadvisors.co

QLV Advisors has four service lines:
1. Outsourced Sales
2. Harbor Ledger Strategic Consulting
3. Gridweave Strategic Consulting
4. QLV VIP

Target Market(s)

event organizers, media companies, corporate event marketers, event tech organizations

Industry/Entity Type

Consulting

Coding

Coded - Design and coding required

Number of Pages Required

5+ page

Font styles to use
Sans Serif

Requirements
Must have
• This will be a website built using Hubspot CMS. If you are not familiar with this, please do not participate as we will not be able to use your designs.
SEO optimized
Landing pages with lead capture leading to content downloads
Each service line needs its own page/s with cta's
Highly visual, modern, bold
Navigational areas: Home, Services, Resources, Events, Blog, About Us
Content formats: video, podcasts, content downloads
Will need at least 4 landing pages in addition to the website for each service line plus templates in case we need to update with new copy
We have or own color palette and logo as well as logos for Harbor Ledger and Gridweave. Those colors must be used.
Font can be modified
We need to have a conversation with the designer that is chosen to go over each service line and also understand what kind of images we should be uploading.
Nice to have
• We would really like the site to reflect the following words:
Bold
Future focused
Results oriented
Hyper focused on the events and event technology sectors (sub sectors: corporate event marketers and B2B media companies).
Should not have
• Flat one page design

```html
<!DOCTYPE html>
<html lang="en">
<head>
<meta charset="utf-8">
<title>QLV Advisors — Discover How We Make an Impact</title>
<link rel="stylesheet" href="https://fonts.googleapis.com/css2?family=Libre+Caslon+Text:wght@400;700&family=Poppins:wght@400;500;600&display=swap">
<style>
:root{
  --orange:#ff4a0a;
  --ink:#1e1e1e;
  --text:#555;
  --muted:#8a8a8a;
  --light:#f6f6f6;
  --line:#ececec;
  --dark:#2a2a2a;
  --white:#fff;
  --serif:"Libre Caslon Text",Georgia,serif;
  --sans:"Poppins",Arial,sans-serif;
}
*{margin:0;padding:0;box-sizing:border-box}
html,body{width:1200px;height:4141px;overflow:hidden}
body{font-family:var(--sans);color:var(--ink);background:var(--white);position:relative}
section,header,footer{position:absolute;left:0;width:1200px}
.abs{position:absolute}
.btn{position:absolute;display:flex;align-items:center;justify-content:center;background:var(--orange);color:var(--white);font-weight:600;font-size:15px;text-decoration:none}
.eyebrow{position:absolute;font-size:16px;color:#333}
.title{position:absolute;font-family:var(--serif);font-size:30px;line-height:39px;color:var(--ink)}
.arrow-btn{position:absolute;width:36px;height:36px;border-radius:50%;display:flex;align-items:center;justify-content:center;background:var(--white);box-shadow:0 3px 10px rgba(0,0,0,.08)}
.arrow-btn.on{background:var(--orange)}
.photo{position:absolute}

/* hero */
.hero{top:0;height:616px;background:linear-gradient(100deg,#5a5e66 0%,#7d838b 40%,#9aa0a6 70%,#6d7178 100%)}
.hero-shade{position:absolute;inset:0;background:linear-gradient(90deg,rgba(20,22,28,.55),rgba(20,22,28,.1) 60%,rgba(20,22,28,.05))}
.hero-person{left:640px;top:110px;width:360px;height:506px;background:linear-gradient(180deg,#3a3838,#1c1b1d);border-radius:160px 160px 0 0;opacity:.85}
.logo{position:absolute;font-family:var(--sans);font-weight:600;font-size:26px;color:var(--orange);letter-spacing:.5px}
.nav{position:absolute;left:427px;top:33px;display:flex;gap:26px;font-size:13px;color:var(--white)}
.chat{position:absolute;left:906px;top:21px;width:112px;height:45px;border:1.5px solid var(--white);color:var(--white);font-size:13px;font-weight:600;display:flex;align-items:center;justify-content:center}
.hero h1{position:absolute;left:183px;top:178px;font-family:var(--serif);font-weight:400;color:var(--white);font-size:48px;line-height:60px}
.hero h1 b{font-size:58px;font-weight:700;display:block;line-height:64px}
.hero p{position:absolute;left:183px;top:330px;width:390px;color:var(--white);font-size:15px;line-height:23px}

/* about */
.about{top:616px;height:621px}
.dots{position:absolute;left:151px;top:401px;width:190px;height:190px;background-image:radial-gradient(#c9c9c9 2px,transparent 2.5px);background-size:23px 23px}
.about-text{position:absolute;left:627px;top:0;width:340px}
.about p{position:absolute;left:627px;top:218px;width:340px;font-size:14.5px;line-height:23.3px;color:var(--text)}

/* services */
.services{top:1237px;height:487px;background:var(--light)}
.card{position:absolute;top:185px;height:220px;width:262px;background:var(--white);border:1px solid var(--line);border-radius:4px;padding:20px 26px}
.card.active{background:var(--orange);border-color:var(--orange);box-shadow:0 10px 24px rgba(255,74,10,.25)}
.card .ico{width:42px;height:42px;border-radius:8px;background:#fdece5;display:flex;align-items:center;justify-content:center;margin-top:0}
.card.active .ico{background:var(--white)}
.card h3{font-size:14.5px;font-weight:600;line-height:21px;margin-top:20px;color:var(--ink)}
.card p{font-size:11.5px;line-height:18px;color:var(--muted);margin-top:6px}
.card a{display:flex;align-items:center;gap:8px;font-size:11.5px;color:var(--orange);margin-top:10px;text-decoration:none}
.card.active h3,.card.active p,.card.active a{color:var(--white)}
.card.active a{font-weight:600}

/* video */
.video{top:1724px;height:507px;background:var(--orange)}
.video-photo{left:0;top:0;width:645px;height:507px;background:linear-gradient(135deg,#c9b6a0,#9c8572 45%,#6e5a4b);clip-path:polygon(0 0,590px 0,645px 507px,0 507px)}
.play{position:absolute;left:266px;top:223px;width:58px;height:58px;border-radius:50%;background:rgba(255,255,255,.55);display:flex;align-items:center;justify-content:center}
.play span{width:34px;height:34px;border-radius:50%;background:var(--white);display:flex;align-items:center;justify-content:center}
.video .eyebrow,.video .title,.video p{color:var(--white)}
.video p{position:absolute;left:683px;top:213px;width:330px;font-size:14.5px;line-height:22.6px}
.watch{position:absolute;left:684px;top:367px;width:142px;height:52px;background:var(--white);color:var(--orange);font-family:var(--serif);font-size:14px;display:flex;align-items:center;justify-content:center}

/* testimonials */
.testimonials{top:2231px;height:604px}
.quote{position:absolute;top:204px;width:405px;height:240px;background:var(--white);box-shadow:0 6px 24px rgba(0,0,0,.06);padding:26px 30px}
.quote .who{display:flex;align-items:center;gap:16px}
.avatar{width:46px;height:46px;border-radius:50%;background:linear-gradient(135deg,#7a5a48,#3a2a22)}
.who b{display:block;font-size:14.5px;font-weight:600}
.who small{font-size:11.5px;color:var(--muted)}
.stars{margin-left:auto;color:#ffb400;font-size:13px;letter-spacing:3px}
.quote p{margin-top:28px;font-size:14px;line-height:22.6px;color:var(--text)}
.pager{position:absolute;top:507px;left:0;width:1200px;height:10px}
.pager i{position:absolute;top:0;width:6px;height:6px;border-radius:50%;background:#bbb}
.pager i.on{background:var(--orange);width:7px;height:7px}

/* blog */
.blog{top:2835px;height:795px;background:#fcfcfc}
.center{left:0;width:1200px;text-align:center}
.post{position:absolute;top:204px;width:262px;height:410px;background:var(--white);box-shadow:0 6px 24px rgba(0,0,0,.05)}
.post .pic{height:206px}
.post h3{margin:26px 26px 0;font-size:14px;line-height:20.5px;font-weight:600}
.post p{margin:12px 26px 0;font-size:11.5px;line-height:20px;color:var(--muted)}
.post a{display:flex;align-items:center;gap:10px;margin:18px 26px 0;font-size:12.5px;color:var(--ink);text-decoration:none}
.post a.hot{color:#2b44c8;font-weight:600}

/* footer */
.footer{top:3630px;height:511px;background:var(--dark);color:var(--white)}
.footer h2{position:absolute;left:183px;top:78px;font-weight:400;font-size:30px;line-height:40px}
.rule{position:absolute;left:183px;top:191px;width:832px;height:1px;background:#444}
.col h4{font-size:14px;font-weight:600}
.col ul{list-style:none;margin-top:30px}
.col li{font-size:12px;line-height:30px;color:#ddd}
.contact li{display:flex;gap:18px;align-items:flex-start;line-height:18px;margin-bottom:19px}
.social{position:absolute;left:183px;top:379px;display:flex;gap:14px}
.social i{width:7px;height:7px;background:#ddd;display:block}
.copy{position:absolute;left:0;width:1200px;top:452px;text-align:center;font-size:11px;color:#ccc}
</style>
</head>
<body>

<header class="hero">
  <div class="photo hero-person" role="img" aria-label="Smiling consultant in a dark blazer with arms crossed, modern office behind"></div>
  <div class="hero-shade" role="img" aria-label="Bright open-plan office with lounge seating and staff at work"></div>
  <div class="logo" style="left:183px;top:18px">QLV<span style="font-size:12px;font-weight:600;margin-left:4px">advisors</span></div>
  <nav class="nav"><span>Home</span><span>Services</span><span>Resources</span><span>Events</span><span>Blog</span><span>About Us</span></nav>
  <div class="chat">Let’s Chat</div>
  <h1>Discover How We<b>Make an Impact</b></h1>
  <p>Lorem ipsum dolor sit amet, consectetur adipisi cing elit tempor incididunt labore.</p>
  <a class="btn" style="left:183px;top:408px;width:137px;height:53px">Get Started</a>
</header>

<section class="about">
  <div class="dots"></div>
  <div class="photo" style="left:185px;top:81px;width:403px;height:458px;background:linear-gradient(135deg,#c79a70,#e7d7c0 50%,#a8805d)" role="img" aria-label="Two colleagues reviewing printed charts at a wooden table"></div>
  <div class="eyebrow" style="left:627px;top:77px;font-size:14px">About Us</div>
  <h2 class="title" style="left:627px;top:118px">Our Approach Is Simple<br>But Not Time-Wasting</h2>
  <p>QLV Advisors helps event and media com panies as well as the technology partners that support them modernize revenue organizations and future proof their businesses. We created and trademarked The Harbor Ledger organizational model to help our customers achieve optimal and consistent sales acceleration.</p>
  <a class="btn" style="left:628px;top:431px;width:137px;height:53px">Read More</a>
</section>

<section class="services">
  <div class="eyebrow" style="left:185px;top:77px">Our Service</div>
  <h2 class="title" style="left:184px;top:112px">Grow Business With Us</h2>
  <div class="arrow-btn" style="left:924px;top:78px"><svg width="10" height="10" viewBox="0 0 10 10"><path d="M6.5 1.5 3 5l3.5 3.5" fill="none" stroke="#333" stroke-width="1.4"/></svg></div>
  <div class="arrow-btn on" style="left:981px;top:78px"><svg width="10" height="10" viewBox="0 0 10 10"><path d="M3.5 1.5 7 5 3.5 8.5" fill="none" stroke="#fff" stroke-width="1.4"/></svg></div>

  <div class="card active" style="left:183px">
    <div class="ico"><svg width="22" height="22" viewBox="0 0 22 22"><path d="M4 15c3-1 5-4 7-7l3 3c-2 3-5 5-8 6z M12 6l4 4 3-3-4-4z" fill="none" stroke="#333" stroke-width="1.4"/></svg></div>
    <h3>Outsourced Sales</h3>
    <p>Lorem ipsum dolor sit amet, consectetur adipisicing elit, sed do eiusmod tempor incididunt</p>
    <a>Read More <svg width="14" height="8" viewBox="0 0 14 8"><path d="M0 4h12M9 1l3 3-3 3" fill="none" stroke="currentColor" stroke-width="1.2"/></svg></a>
  </div>
  <div class="card" style="left:469px">
    <div class="ico"><svg width="18" height="20" viewBox="0 0 18 20"><rect x="2" y="2" width="14" height="16" rx="1.5" fill="none" stroke="#ff4a0a" stroke-width="1.3"/><path d="M5 7h8M5 10h8M5 13h8" stroke="#ff4a0a" stroke-width="1.2"/></svg></div>
    <h3>Harbor Ledger Strategic Consulting</h3>
    <p>Lorem ipsum dolor sit amet con sectetur adipisicing elit.</p>
    <a>Read More <svg width="14" height="8" viewBox="0 0 14 8"><path d="M0 4h12M9 1l3 3-3 3" fill="none" stroke="currentColor" stroke-width="1.2"/></svg></a>
  </div>
  <div class="card" style="left:755px">
    <div class="ico"><svg width="20" height="18" viewBox="0 0 20 18"><path d="M3 3h14v9H8l-4 3v-3H3z" fill="none" stroke="#ff4a0a" stroke-width="1.3"/><path d="M7 7.5h6" stroke="#ff4a0a" stroke-width="1.2"/></svg></div>
    <h3>Gridweave Strategic Consulting</h3>
    <p>Lorem ipsum dolor sit amet, cons ectetur adipisicing elit, sed do eiu</p>
    <a>Read More <svg width="14" height="8" viewBox="0 0 14 8"><path d="M0 4h12M9 1l3 3-3 3" fill="none" stroke="currentColor" stroke-width="1.2"/></svg></a>
  </div>
</section>

<section class="video">
  <div class="photo video-photo" role="img" aria-label="Group of smiling colleagues gathered around a laptop"></div>
  <div class="play"><span><svg width="10" height="12" viewBox="0 0 10 12"><path d="M1 1l8 5-8 5z" fill="#ff4a0a"/></svg></span></div>
  <div class="eyebrow" style="left:683px;top:75px;font-size:14.5px">Explore Videos</div>
  <h2 class="title" style="left:683px;top:120px">We are your<br>Business Maker</h2>
  <p>Lorem ipsum dolor sit amet, consectetur adipiscing elit, sed do eiusmod tempor incididunt ut labore et dolore magna aliqua. Quis ipsum suspendisse ultrices gravida. Risus commodo viverra maecenas</p>
  <div class="watch">Watch Now!</div>
</section>

<section class="testimonials">
  <div class="eyebrow" style="left:183px;top:78px;font-size:15px">Testimonial</div>
  <h2 class="title" style="left:183px;top:120px">What Our Clients Say</h2>
  <div class="arrow-btn" style="left:924px;top:79px"><svg width="10" height="10" viewBox="0 0 10 10"><path d="M6.5 1.5 3 5l3.5 3.5" fill="none" stroke="#333" stroke-width="1.4"/></svg></div>
  <div class="arrow-btn on" style="left:981px;top:79px"><svg width="10" height="10" viewBox="0 0 10 10"><path d="M3.5 1.5 7 5 3.5 8.5" fill="none" stroke="#fff" stroke-width="1.4"/></svg></div>

  <div class="quote" style="left:183px">
    <div class="who"><div class="avatar" role="img" aria-label="Client portrait"></div><div><b>John Doe</b><small>Satisfied Clients</small></div><div class="stars">★★★★★</div></div>
    <p>Lorem ipsum dolor sit amet, consectetur adipisicing elit, sed do eiusmod tempor incididunt ut labore et dolore magna aliqua. Ut enim ad minim veniam, quis nostrud exercitation ullamco laboris nisi ut.</p>
  </div>
  <div class="quote" style="left:610px">
    <div class="who"><div class="avatar" role="img" aria-label="Client portrait"></div><div><b>Dua Smith</b><small>Satisfied Clients</small></div><div class="stars">★★★★★</div></div>
    <p>Lorem ipsum dolor sit amet, consectetur adipisicing elit, sed do eiusmod tempor incididunt ut labore et dolore magna aliqua. Ut enim ad minim veniam, quis nostrud exercitation ullamco. laboris nisi ut aliquip ex</p>
  </div>
  <div class="pager"><i class="on" style="left:562px"></i><i style="left:593px"></i><i style="left:614px"></i><i style="left:633px"></i></div>
</section>

<section class="blog">
  <div class="eyebrow center" style="top:78px;font-size:15px">Our News</div>
  <h2 class="title center" style="top:118px">Recent Blog Posts</h2>

  <article class="post" style="left:183px">
    <div class="pic" style="background:linear-gradient(135deg,#b88a63,#e5d3bd 55%,#7a5a43)" role="img" aria-label="Team meeting around laptops in a bright office"></div>
    <h3>Three Ways to Monetize Hybrid Events: A Presen tation By Stephan.</h3>
    <p>Lorem ipsum dolor sit amet, consectetur adipiscing elit, sed</p>
    <a class="hot">Read More <svg width="18" height="8" viewBox="0 0 18 8"><path d="M0 4h16M13 1l3 3-3 3" fill="none" stroke="currentColor" stroke-width="1.2"/></svg></a>
  </article>
  <article class="post" style="left:469px">
    <div class="pic" style="background:linear-gradient(135deg,#d9cfc3,#a99480 55%,#5e4a3d)" role="img" aria-label="Colleagues shaking hands in an office"></div>
    <h3>Startup Mindset: Reinve nting Company Structure and Event Identity.</h3>
    <p>Lorem ipsum dolor sit amet, consectetur adipiscing elit, sed</p>
    <a>Read More <svg width="18" height="8" viewBox="0 0 18 8"><path d="M0 4h16M13 1l3 3-3 3" fill="none" stroke="currentColor" stroke-width="1.2"/></svg></a>
  </article>
  <article class="post" style="left:755px">
    <div class="pic" style="background:linear-gradient(135deg,#7b5a44,#a57d5c 50%,#4a3a30)" role="img" aria-label="Overhead view of a team joining hands over a wooden table"></div>
    <h3>QLV Recommendations for Virtual Class Vendors How to Engage Attendees.</h3>
    <p>Lorem ipsum dolor sit amet, consectetur adipiscing elit, sed</p>
    <a>Read More <svg width="18" height="8" viewBox="0 0 18 8"><path d="M0 4h16M13 1l3 3-3 3" fill="none" stroke="currentColor" stroke-width="1.2"/></svg></a>
  </article>

  <a class="btn" style="left:529px;top:659px;width:142px;height:53px">View More</a>
</section>

<footer class="footer">
  <h2>Looking For The Best Business<br>Consulltation?</h2>
  <a class="btn" style="left:879px;top:82px;width:135px;height:49px;font-size:12.5px">Contact Us!</a>
  <div class="rule"></div>

  <div class="logo" style="left:183px;top:230px;font-size:24px">QLV<span style="font-size:11px;font-weight:600;margin-left:4px">advisors</span></div>
  <p class="abs" style="left:183px;top:309px;width:190px;font-size:11.5px;line-height:18px;color:#ddd">Lorem ipsum dolor sit amet, con sectetur adipisicing elited do eiusmod tempor.</p>
  <div class="social"><i></i><i></i><i></i><i></i></div>

  <div class="col abs" style="left:448px;top:236px"><h4>Quick Links</h4><ul><li>Home</li><li>Service</li><li>About</li><li>Resources</li></ul></div>
  <div class="col abs" style="left:606px;top:236px"><h4>Help</h4><ul><li>Events</li><li>Blog</li><li>Contact</li><li>Privacy policy</li></ul></div>
  <div class="col contact abs" style="left:744px;top:236px;width:220px"><h4>Contact Us</h4>
    <ul>
      <li><svg width="12" height="12" viewBox="0 0 12 12"><path d="M3 1l2 2.5-1.2 1.3a7 7 0 0 0 3.4 3.4L8.5 7 11 9l-1 2C5 11 1 7 1 2z" fill="none" stroke="#aaa" stroke-width="1"/></svg>987 - 555 - 210</li>
      <li><svg width="12" height="10" viewBox="0 0 12 10"><rect x="1" y="1" width="10" height="8" fill="none" stroke="#aaa"/><path d="M1 1l5 4 5-4" fill="none" stroke="#aaa"/></svg>hello@qlvmail.co</li>
      <li><svg width="10" height="13" viewBox="0 0 10 13"><path d="M5 12S1 7.5 1 5a4 4 0 0 1 8 0c0 2.5-4 7-4 7z" fill="none" stroke="#aaa"/><circle cx="5" cy="5" r="1.4" fill="#aaa"/></svg>Lorem ipsum dolor sit amet,<br>consectetur adipiscing elit,</li>
    </ul>
  </div>

  <div class="copy">Copyright © 2021 qlvadvisors.co All rights reserved</div>
</footer>

</body>
</html>
```